Business Card Design Project

The overall design must be suitable alongside our company logo which is attached

There must be space for the agent to write their name & telephone number

Card must contain the words:

Maple Carpet Cleaning

Agent:
Tel:

Target Market(s)

Industry/Entity Type

Business

```html
<!DOCTYPE html>
<html lang="en">
<head>
<meta charset="utf-8">
<title>Maple Carpet Cleaning – Agent Card</title>
<link rel="stylesheet" href="https://fonts.googleapis.com/css2?family=Arimo:wght@400;700&display=swap">
<style>
  :root {
    --page-bg: #ffffff;
    --card-light-top: #e9e9e9;
    --card-light-bottom: #ffffff;
    --card-dark: #241a14;
    --gold: #d8a94a;
    --gold-deep: #8a5a1c;
    --band-dark: #3a2616;
    --brand-ink: #1d1612;
    --field-bg: #ffffff;
  }
  * { box-sizing: border-box; margin: 0; padding: 0; }
  html, body {
    width: 1200px;
    height: 900px;
    overflow: hidden;
    background: var(--page-bg);
    font-family: "Arimo", Arial, sans-serif;
  }
  .business-card {
    position: absolute;
    left: 101px;
    top: 160px;
    width: 998px;
    height: 581px;
    display: flex;
    flex-direction: column;
    box-shadow: 0 6px 18px rgba(0,0,0,0.12);
  }
  .card-header {
    height: 317px;
    background: linear-gradient(to bottom, var(--card-light-top), var(--card-light-bottom) 70%);
    display: flex;
    align-items: center;
    padding-left: 52px;
  }
  .brand {
    display: flex;
    align-items: center;
    gap: 22px;
  }
  .brand-mark {
    width: 40px;
    height: 40px;
    border-radius: 50%;
    background: var(--gold);
  }
  .brand-name {
    font-size: 54px;
    font-weight: 700;
    color: var(--brand-ink);
    letter-spacing: 0.5px;
  }
  .ornament-band {
    height: 26px;
    background: linear-gradient(to bottom, var(--band-dark), var(--gold-deep) 50%, var(--band-dark));
  }
  .card-body {
    flex: 1;
    background: var(--card-dark);
    padding: 46px 0 0 47px;
  }
  .field-row {
    display: flex;
    align-items: center;
    height: 41px;
    margin-bottom: 21px;
  }
  .field-label {
    width: 121px;
    display: flex;
    justify-content: space-between;
    padding-right: 10px;
    font-size: 32px;
    color: var(--gold);
  }
  .field-line {
    height: 41px;
    background: var(--field-bg);
    border: 2px solid var(--gold);
  }
  .field-line--agent { width: 593px; }
  .field-line--tel { width: 341px; }
</style>
</head>
<body>
  <main class="business-card">
    <header class="card-header">
      <div class="brand">
        <span class="brand-mark" aria-hidden="true"></span>
        <span class="brand-name">Maple Carpet Cleaning</span>
      </div>
    </header>
    <div class="ornament-band" role="img" aria-label="Decorative gold ornamental border"></div>
    <section class="card-body">
      <div class="field-row">
        <span class="field-label"><span>Agent</span><span>:</span></span>
        <span class="field-line field-line--agent"></span>
      </div>
      <div class="field-row">
        <span class="field-label"><span>Tel</span><span>:</span></span>
        <span class="field-line field-line--tel"></span>
      </div>
    </section>
  </main>
</body>
</html>
```